Horse related business entrepreneur needs a business card

I need a business card design for my horse related business. The enterprise is Copper Vale LLC and I have 3 businesses (headquartered at 2 locations): 1. property management where we rent horse stalls and apartments at a thoroughbred training center outside Ocala; 2. a medium sized transportation service in central Florida that sells horse bedding and removes used horse bedding from horse farms; and horse racing

```html
<!DOCTYPE html>
<html lang="en">
<head>
<meta charset="utf-8">
<title>Copper Vale Farm – Business Card</title>
<link rel="stylesheet" href="https://fonts.googleapis.com/css2?family=Questrial&family=Quicksand:wght@500;700&display=swap">
<style>
  :root {
    --teal: #0f5775;
    --orange: #e0733f;
    --peach: #f6dccb;
    --mist: #c9ced3;
    --ink: #3a3a3a;
    --paper: #ffffff;
    --backdrop: #e6e8ea;
  }
  * { box-sizing: border-box; margin: 0; padding: 0; }
  html, body { width: 1200px; height: 900px; overflow: hidden; }
  body {
    background: var(--backdrop);
    font-family: "Questrial", sans-serif;
    color: var(--ink);
    position: relative;
  }
  .card {
    position: absolute;
    left: 320px;
    width: 560px;
    height: 320px;
    background: var(--paper);
    border-radius: 22px;
    overflow: hidden;
    box-shadow: 0 6px 18px rgba(0,0,0,0.15);
  }
  .card--front { top: 95px; }
  .card--back { top: 485px; }

  .brand {
    display: flex;
    align-items: center;
    gap: 10px;
    font-family: "Questrial", sans-serif;
    font-size: 26px;
    letter-spacing: 3px;
    color: var(--teal);
    text-transform: uppercase;
  }
  .brand__dot {
    width: 14px; height: 14px;
    border-radius: 50%;
    background: var(--orange);
  }
  .brand__place {
    font-size: 15px;
    color: var(--orange);
    letter-spacing: 1px;
    margin-top: 4px;
  }

  /* Front */
  .front__brand { position: absolute; top: 48px; left: 0; right: 0; display: flex; flex-direction: column; align-items: center; }
  .front__rule { position: absolute; left: 150px; width: 260px; height: 1.5px; background: var(--orange); }
  .front__rule--top { top: 118px; }
  .front__rule--bottom { top: 196px; }
  .front__person { position: absolute; top: 132px; left: 0; right: 0; text-align: center; }
  .person__name { font-family: "Quicksand", sans-serif; font-weight: 700; font-size: 26px; color: var(--teal); }
  .person__role { font-family: "Quicksand", sans-serif; font-weight: 500; font-size: 18px; color: var(--ink); margin-left: 6px; }
  .person__company { font-size: 14px; margin-top: 6px; }
  .contact-band {
    position: absolute; left: 0; right: 0; bottom: 0; height: 50px;
    background: var(--teal);
    display: flex; align-items: center; justify-content: center; gap: 22px;
    color: var(--paper); font-size: 15px;
  }
  .contact-band__item { display: flex; align-items: center; gap: 6px; }
  .contact-band svg { width: 14px; height: 14px; fill: var(--paper); }

  /* Back */
  .back__art {
    position: absolute; right: 0; top: 0; width: 330px; height: 320px;
    background: linear-gradient(120deg, rgba(201,206,211,0.75) 0%, rgba(201,206,211,0.4) 35%, var(--peach) 60%, rgba(246,220,203,0.6) 100%);
  }
  .back__brand { position: absolute; top: 34px; right: 60px; display: flex; flex-direction: column; align-items: center; }
  .back__addresses { position: absolute; left: 44px; top: 130px; font-size: 17px; line-height: 1.35; }
  .address { display: block; }
  .address--second { margin-top: 48px; }
  .back__pin { position: absolute; left: 190px; top: 182px; width: 26px; height: 32px; }
</style>
</head>
<body>

<section class="card card--front">
  <div class="front__brand">
    <div class="brand"><span class="brand__dot"></span>Copper Vale Farm</div>
    <div class="brand__place">Fernwood FL</div>
  </div>
  <div class="front__rule front__rule--top"></div>
  <div class="front__person">
    <div><span class="person__name">Dale Harmon</span><span class="person__role">Owner</span></div>
    <div class="person__company">Copper Vale LLC (an equine conglomerate)</div>
  </div>
  <div class="front__rule front__rule--bottom"></div>
  <div class="contact-band">
    <span class="contact-band__item">
      <svg viewBox="0 0 16 16"><path d="M1 3h14v10H1z M1 3l7 6 7-6" fill="none" stroke="#fff" stroke-width="1.6"/></svg>
      dale@coppervale.com
    </span>
    <span class="contact-band__item">
      <svg viewBox="0 0 16 16"><path d="M4 1l2.5 3.5-1.5 1.5c1 2 3 4 5 5l1.5-1.5L15 12l-2 3C7 14 2 9 1 3z"/></svg>
      (555) 014-2281
    </span>
    <span class="contact-band__item">
      <svg viewBox="0 0 16 16"><path d="M4 1h7v4H4z M2 6h12v6h-2v3H4v-3H2z"/></svg>
      (555) 014-7730
    </span>
  </div>
</section>

<section class="card card--back">
  <div class="back__art" role="img" aria-label="Large faint silhouettes of galloping horses in peach and grey"></div>
  <div class="back__brand">
    <div class="brand"><span class="brand__dot"></span>Copper Vale Farm</div>
    <div class="brand__place">Fernwood FL</div>
  </div>
  <div class="back__addresses">
    <span class="address">1520 SE 92nd Lane<br>Fernwood, FL 32600</span>
    <span class="address address--second">780 Alder Ridge Road<br>Linden, VA 22900</span>
  </div>
  <svg class="back__pin" viewBox="0 0 26 32" aria-hidden="true">
    <path d="M13 2a9 9 0 0 0-9 9c0 7 9 15 9 15s9-8 9-15a9 9 0 0 0-9-9z" fill="var(--orange)"/>
    <circle cx="13" cy="11" r="3.5" fill="#fff"/>
    <ellipse cx="13" cy="29" rx="9" ry="2" fill="none" stroke="var(--orange)" stroke-width="1.2"/>
  </svg>
</section>

</body>
</html>
```